Business Card design for Property Developer

We need a business card design for a Melbourne based Property Developer called "Kestrel Grove Pty Ltd".

We subdivide land and onsell to builders etc.

We already have a company logo, which is attached. Also I have attached the layout requirements from the printer. We would like a 2-sided design with one side displaying our logo by itself and the other with the required info, such as name, address, tel no., email, abn etc. The card will need to be used by 4 members of staff so name and contact details should be interchangable.
Updates

If possible, can you please write "name' "job position" "phone" "email" "address" on the card but leave them so I can add the details at a later time. Thank you. Also I plan on printing with UV spot printing as a background on the card. Keep this is mind when designing.

Thanks again.

Hello designers, please do not include pics of houses, house plansĀ or construction machinery etc as we really do not like the way it looks. Thank you.

Target Market(s)

Real Estate Agents, Land Owners, Local Council Departments, Govt Bodies, other Developers etc.

Industry/Entity Type

Business

Requirements
Must have
• 2-sided design with one side displaying our logo by itself and the other with the required info, such as name, address, tel no., email, abn etc.

```html
<!DOCTYPE html>
<html lang="en">
<head>
<meta charset="utf-8">
<title>Kestrel Grove – Business Card</title>
<link rel="stylesheet" href="https://fonts.googleapis.com/css2?family=Open+Sans:wght@400;700&display=swap">
<style>
  :root {
    --page-bg: #e4e4e4;
    --card-bg: #ffffff;
    --ink: #333333;
    --ink-name: #444444;
    --ink-muted: #555555;
    --brand-red: #c8202f;
    --mark-dark: #222222;
    --fold-blue: #29abe2;
  }
  * { margin: 0; padding: 0; box-sizing: border-box; }
  html, body {
    width: 1200px;
    height: 1033px;
    overflow: hidden;
    background: var(--page-bg);
    font-family: "Open Sans", Arial, sans-serif;
  }
  .business-card {
    position: absolute;
    left: 214px;
    top: 278px;
    width: 772px;
    height: 477px;
    background: var(--card-bg);
  }
  .card-front {
    position: absolute;
    left: 0;
    top: 0;
    width: 772px;
    height: 241px;
  }
  .brand-block {
    position: absolute;
    left: 447px;
    top: 40px;
    width: 240px;
    height: 170px;
    transform: rotate(180deg);
    display: flex;
    flex-direction: column-reverse;
    align-items: center;
    justify-content: space-between;
  }
  .brand-name {
    font-size: 27px;
    font-weight: 700;
    color: var(--brand-red);
    letter-spacing: 0.5px;
    white-space: nowrap;
  }
  .brand-dot {
    width: 98px;
    height: 98px;
    border-radius: 50%;
    background: var(--mark-dark);
  }
  .fold-line {
    position: absolute;
    left: 6px;
    top: 238px;
    width: 766px;
    height: 6px;
  }
  .contact-details {
    position: absolute;
    right: 387px;
    top: 280px;
    text-align: right;
    font-size: 23px;
    line-height: 31px;
    color: var(--ink);
    white-space: nowrap;
  }
  .holder {
    position: absolute;
    left: 562px;
    top: 334px;
    transform: translateX(-50%);
    text-align: center;
    white-space: nowrap;
  }
  .holder-name {
    font-size: 23px;
    font-weight: 700;
    color: var(--ink-name);
    line-height: 28px;
  }
  .holder-role {
    font-size: 19px;
    color: var(--ink-muted);
    line-height: 24px;
  }
</style>
</head>
<body>
  <main class="business-card">
    <section class="card-front">
      <div class="brand-block">
        <span class="brand-name">KESTREL GROVE</span>
        <span class="brand-dot"></span>
      </div>
    </section>

    <svg class="fold-line" viewBox="0 0 766 6" aria-hidden="true">
      <line x1="0" y1="3" x2="766" y2="3" stroke="var(--fold-blue)" stroke-width="6" stroke-dasharray="35 25"/>
    </svg>

    <address class="contact-details" style="font-style: normal;">
      <div>418 Larkspur Avenue, #212</div>
      <div>Melbourne, VIC 3004-1180</div>
      <div>tel. 5310 2874 / 6142 9035</div>
      <div>fax. 5267 3190 / 8416 5523</div>
      <div>rowan@kestrel-grove.com</div>
    </address>

    <div class="holder">
      <div class="holder-name">ROWAN ASHBY</div>
      <div class="holder-role">manager</div>
    </div>
  </main>
</body>
</html>
```